A high tech startup is crawing for an awesome business card design

First of all, we commit to give you clear and rapid feedback. If we don't think you are on the right track we will let you know right away.

We are looking for appealing and eye catching business card design for a high tech company based in San Francisco and Zagreb.

Nortavo believes in the future of NFC technology, in a world that is increasingly dominated by the endless possibilities of mobile phones and contactless solutions.

We develop innovative NFC-based solutions to event organizers for ticket validation, queue management, real-time analytic and cashless payment. Also, we save visitors from unnecessary queues so they can better spend their time on the event and share their experience with others beyond the physical boundaries of the event.

Please look for more about Nortavo and our solutions at http://www-gravilux-example.com and www.facebook.com/gravilux

Out-of-the-box
Please note that we also attached a special squarish and circular "logo". We print this only on NFC tags that we paste on accreditations or event tickets. It would be nice if we could occasionally put such square or circular NFC tags on our business cards as well. NFC tags are either 29, 34 or 38 mm in diameter. Since such tags are expensive we are not planning to put them on every business card. What you want to put on NFC tag is up to you, i.e. Nortavo logo, NFC industry logo etc.
So you have 3 options:
a) to merge a logo placement with space for NFC tag
b) to separate placement of NFC tag from logo space
c) to completely dismiss the idea of having NFC tag on business
card and skip this out-of-the-box assignment :)

We are looking forward to see your suggestions!

You don`t need to stick to Arial we used with our logo. You can choose any other if it is clean and simple like Sans Serif etc.

Design the business card using a vector format.
Final files to be turned over as EPS, AI (CSS5) and JPG.
Information to be included on card: logo, website, phone number, person's title, and email. We might need some space for business address but not for now. One side of card should not be completely in dark color as we want our clients to be able to write down something on card.
Please use the attached logo in the design (logo can also be provided in other file formats).

Font styles to use
Sans Serif
Other font styles liked:
• Segoe UI Light, Calibri or smth similar

Requirements
Must have
• The final design should communicate innovativeness, flexibility and cutting edge technology.
• We would like to receive designs with the following elements:
• Simple ++
• Creative ++
• Modern ++
• Unique ++
• Professional ++
• Easy to read ++
• Simple and modern font ++
• Thicker paper ++
• Double side ++
Nice to have
• We would like to receive designs with some of the following elements:
• Rounded edges +
• Textured paper +
• Embossed/Letterpress +
Should not have
• Heavy graphic

```html
<!DOCTYPE html>
<html lang="en">
<head>
<meta charset="utf-8">
<title>Nortavo Business Card</title>
<link rel="stylesheet" href="https://fonts.googleapis.com/css2?family=Open+Sans:wght@400;700&display=swap">
<style>
  :root {
    --backdrop: #ecebe8;
    --card-blue: #2a9dc8;
    --card-ink: #ffffff;
    --card-shadow: rgba(0, 0, 0, 0.18);
  }
  * { margin: 0; padding: 0; box-sizing: border-box; }
  html, body {
    width: 1200px;
    height: 800px;
    overflow: hidden;
    background: var(--backdrop);
  }
  .stage {
    width: 1200px;
    height: 800px;
    display: flex;
    align-items: center;
    justify-content: center;
  }
  .business-card {
    position: relative;
    width: 900px;
    height: 520px;
    background: var(--card-blue);
    border-top-right-radius: 170px;
    box-shadow: 0 10px 30px var(--card-shadow);
    color: var(--card-ink);
    font-family: "Open Sans", "Segoe UI", sans-serif;
  }
  .brand-name {
    position: absolute;
    left: 60px;
    right: 0;
    top: 200px;
    text-align: center;
    font-weight: 700;
    font-size: 78px;
    letter-spacing: 5px;
    line-height: 1;
    text-transform: uppercase;
  }
  .locations {
    position: absolute;
    left: 36px;
    bottom: 52px;
    display: flex;
    align-items: center;
    gap: 30px;
    font-size: 20px;
    letter-spacing: 3px;
    text-transform: uppercase;
  }
  .location { font-weight: 400; white-space: nowrap; }
  .location-region { font-weight: 700; }
  .location-divider {
    width: 2px;
    height: 56px;
    background: var(--card-ink);
    opacity: 0.85;
  }
</style>
</head>
<body>
  <main class="stage">
    <section class="business-card" aria-label="Nortavo business card">
      <h1 class="brand-name">Nortavo</h1>
      <div class="locations">
        <p class="location">Alder Point <span class="location-region">Westcoast</span></p>
        <span class="location-divider" aria-hidden="true"></span>
        <p class="location">Kestrava <span class="location-region">Southland</span></p>
      </div>
    </section>
  </main>
</body>
</html>
```